A year in review booklet 12 page square mini booklet

a 12 page (including front and back cover) booklet 4.75 inches square.
Front Cover page (page 1)
Something that says WLGTC 2018 ministry year in review or something like that
Image of baptism/missions/etc
Intro Letter from Gordon (page 2) (text to be filled in later)
His headshot image (uploaded)
Quick note about year end giving (to be filled in later)
Sermon Listens (page 3)
Total # of sermon listens at the top (5800)
headphone icon
key at the bottom that says "headphone icon = X listens)
Try to fill most of the page with icons
Lantern Effort Houses Visited (pages 4 & 5)
Total # of houses visited at the top (23,899)
house icon
key at the bottom that says "house icon = 50? houses)
Babies Saved (page 6)
Total # of babies at the top (265)
baby icon
no key at the bottom make every baby = 1 icon
Tons of food served at Whitcombe Outreach (page 7)
Total # of food distributed at the top (500 tons)
bread loaf icon
key at the bottom that says "bread icon = 1 ton, 1000 lbs?, 100 lbs?)
Mission Trips Taken (pages 8&9)
Total # of mission trips taken at the top (11 trips)
airplane icon

Salvations (page 10)
Total # of salvations at the top (150 salvations)
cross icon
no key at the bottom make every salvation = 1 icon
Baptisms (page 11)
Total # of baptisms at the top 22
water droplet
no key at the bottom make every baptism = 1 icon

Back Cover page (page 12)
Give online shortlink (filled in later)
Give through month of December info

Target Market(s)

Church Congregation

Requirements
Must have
• Good graphics

```html
<!DOCTYPE html>
<html lang="en">
<head>
<meta charset="utf-8">
<title>WLGTC 2018 Year in Review – Front Cover</title>
<link rel="stylesheet" href="https://fonts.googleapis.com/css2?family=Prata&family=Montserrat:wght@300;600&display=swap">
<style>
  :root {
    --navy: #1d3767;
    --lavender: #97a0c4;
    --paper: #ffffff;
    --ink: #2f2f33;
    --photo-warm: #e6d6b8;
    --photo-sand: #cdbf9f;
    --photo-slate: #6f8798;
    --photo-teal: #86b9b2;
    --photo-green: #55703c;
    --photo-deep: #3e5a33;
  }
  html, body {
    margin: 0;
    padding: 0;
    overflow: hidden;
    background: var(--paper);
  }
  .cover {
    position: relative;
    width: 1200px;
    height: 1200px;
    overflow: hidden;
    background: var(--paper);
  }
  .cover-shapes {
    position: absolute;
    inset: 0;
  }
  .cover-title {
    position: absolute;
    right: 52px;
    top: 22px;
    margin: 0;
    text-align: right;
    color: var(--paper);
    font-weight: normal;
  }
  .cover-year {
    display: block;
    font-family: "Prata", Georgia, serif;
    font-weight: 400;
    font-size: 162px;
    line-height: 1;
    letter-spacing: -1px;
  }
  .cover-subtitle {
    display: block;
    margin-top: 4px;
    font-family: "Montserrat", Arial, sans-serif;
    font-weight: 300;
    font-size: 42px;
    line-height: 1;
    letter-spacing: 0.5px;
  }
  .church-name {
    position: absolute;
    left: 64px;
    top: 1010px;
    display: flex;
    align-items: center;
    gap: 18px;
  }
  .church-name__dot {
    width: 44px;
    height: 44px;
    border-radius: 50%;
    background: var(--navy);
    flex: none;
  }
  .church-name__text {
    font-family: "Montserrat", Arial, sans-serif;
    font-weight: 600;
    color: var(--navy);
    font-size: 24px;
    line-height: 1.25;
    letter-spacing: 0.5px;
  }
  .church-name__text strong {
    display: block;
    font-weight: 600;
    font-size: 58px;
    line-height: 1;
    letter-spacing: 2px;
  }
  .cover-web {
    position: absolute;
    right: 52px;
    top: 1106px;
    margin: 0;
    font-family: "Montserrat", Arial, sans-serif;
    font-weight: 300;
    font-size: 46px;
    line-height: 1;
    color: var(--ink);
  }
</style>
</head>
<body>
<main class="cover">
  <svg class="cover-shapes" width="1200" height="1200" viewBox="0 0 1200 1200" xmlns="http://www.w3.org/2000/svg">
    <defs>
      <clipPath id="photo-shape">
        <path d="M0,200 Q220,50 560,0 L1200,0 L1200,984 Q500,930 0,760 Z"/>
      </clipPath>
      <linearGradient id="photo-base" x1="0" y1="0" x2="1" y2="1">
        <stop offset="0" stop-color="var(--photo-sand)"/>
        <stop offset="0.45" stop-color="var(--photo-slate)"/>
        <stop offset="0.75" stop-color="var(--photo-green)"/>
        <stop offset="1" stop-color="var(--photo-deep)"/>
      </linearGradient>
      <radialGradient id="photo-light" cx="0.25" cy="0.2" r="0.45">
        <stop offset="0" stop-color="var(--photo-warm)" stop-opacity="0.95"/>
        <stop offset="1" stop-color="var(--photo-warm)" stop-opacity="0"/>
      </radialGradient>
      <radialGradient id="photo-sky" cx="0.85" cy="0.15" r="0.4">
        <stop offset="0" stop-color="var(--photo-teal)" stop-opacity="0.9"/>
        <stop offset="1" stop-color="var(--photo-teal)" stop-opacity="0"/>
      </radialGradient>
      <radialGradient id="photo-center" cx="0.5" cy="0.5" r="0.22">
        <stop offset="0" stop-color="#e9cdb4" stop-opacity="0.8"/>
        <stop offset="1" stop-color="#e9cdb4" stop-opacity="0"/>
      </radialGradient>
    </defs>

    <path class="band-navy" d="M0,0 L500,0 Q180,60 0,184 Z" fill="var(--navy)"/>

    <g class="cover-photo" clip-path="url(#photo-shape)" role="img" aria-label="Cover photo: praying hands resting on an open Bible, blended with a green mountain landscape under a soft sky">
      <rect x="0" y="0" width="1200" height="1000" fill="url(#photo-base)"/>
      <rect x="0" y="0" width="1200" height="1000" fill="url(#photo-light)"/>
      <rect x="0" y="0" width="1200" height="1000" fill="url(#photo-sky)"/>
      <rect x="0" y="0" width="1200" height="1000" fill="url(#photo-center)"/>
    </g>

    <path class="band-lavender" d="M0,768 Q500,950 1200,998 L1200,1072 Q480,1030 0,840 Z" fill="var(--lavender)"/>
  </svg>

  <h1 class="cover-title">
    <span class="cover-year">2018</span>
    <span class="cover-subtitle">YEAR IN REVIEW</span>
  </h1>

  <div class="church-name">
    <span class="church-name__dot"></span>
    <span class="church-name__text"><strong>WLGTC</strong>West Lake Grace<br>Tabernacle Church</span>
  </div>

  <p class="cover-web">www.wlgtc.com</p>
</main>
</body>
</html>
```